Photography and Videography - Tidewell Studios - New Business Card Design

Tidewell Studios is a photography and Videography Company started by creative couple Rory K and Lena P and based on the Sunshine Coast in Queensland, Australia.
We're quirky, creative and innovative people and would like a business card that keeps you looking for more than just a few seconds.
Design wise we would like a black or charcoal background with a bit of a funkier design than just a boring old rectangle shape. Perhaps curved on an edge.
Ideally we would like to be able to make a collage of all of our best photos on the reverse side of the card with the company name or logo and "catch you by the tidewell..." (possibly in italics) underneath it.
On the front of the business card we would like our company name -
"Tidewell Studios", our motto- "Bringing Ideas To Life..." (possibly in italics) and our contact information. The background should be a darker colour like black or charcoal.
We like the look of having contact company details and contact info to one side (right) and a black and white photo of Rory K and Lena P to the other side (left).
Thank you and Good Luck!
Industry/Entity Type
Business
Contact Information for Business Card
Business Name - Tidewell Studios
Slogan - Bring Ideas To life
Name - Rory K | Lena P
Description - Photography | Videography
Phone - 0452 867 213 | 0438 926 057
Email - tidewellstudios@mailbox-example.com.au
Website - www.tidewellstudios-example.com.au
Like us on Friendhub (symbol)
Logo styles of interest
Pictorial/Combination Logo
Look and feel

```html
<!DOCTYPE html>
<html lang="en">
<head>
<meta charset="utf-8">
<title>Tidewell Studios – Business Card</title>
<link rel="stylesheet" href="https://fonts.googleapis.com/css2?family=Audiowide&family=Lora:ital,wght@0,400;0,700;1,400&family=Questrial&display=swap">
<style>
  :root {
    --backdrop: #2a2522;
    --card-charcoal: #262626;
    --card-charcoal-deep: #1c1c1c;
    --title-white: #f2f2f2;
    --tagline-grey: #8a8a8a;
    --name-grey: #b5b5b5;
    --detail-grey: #c9c9c9;
    --rule-grey: #6a6a6a;
    --square-blue: #3b5998;
  }
  * { box-sizing: border-box; margin: 0; padding: 0; }
  html, body { width: 1200px; height: 900px; overflow: hidden; }
  body { background: var(--backdrop); position: relative; }

  .card {
    position: absolute;
    border-radius: 26px;
    overflow: hidden;
    box-shadow: 0 14px 30px rgba(0,0,0,.45);
  }

  /* reverse side */
  .card--back { left: 60px; top: 40px; width: 640px; height: 380px; }
  .collage {
    width: 100%; height: 100%;
    background: linear-gradient(120deg, #5e7fa8 0%, #c9b9a4 22%, #e0672a 40%, #6a5a48 55%, #f0a040 70%, #7a8a96 86%, #d8cfc2 100%);
  }

  /* front side */
  .card--front {
    left: 450px; top: 450px; width: 710px; height: 400px;
    background: linear-gradient(160deg, var(--card-charcoal), var(--card-charcoal-deep));
    display: flex;
  }
  .portrait {
    flex: 0 0 250px; height: 100%;
    background: radial-gradient(ellipse at 50% 45%, #c8c8c8 0%, #8e8e8e 45%, #3a3a3a 100%);
    box-shadow: 4px 0 10px rgba(0,0,0,.5);
  }
  .details { flex: 1; position: relative; padding: 34px 24px 0 30px; white-space: nowrap; }

  .brand {
    font-family: "Audiowide", sans-serif;
    font-size: 32px; font-weight: 400; color: var(--title-white);
    letter-spacing: 1px; text-align: center;
  }
  .tagline {
    font-family: "Lora", serif; font-style: italic;
    font-size: 18px; color: var(--tagline-grey);
    text-align: center; margin-top: 2px; letter-spacing: .5px;
  }

  .team { display: flex; justify-content: center; margin-top: 48px; }
  .member { text-align: center; padding: 0 26px; flex: 0 0 auto; }
  .member + .member { border-left: 2px solid var(--rule-grey); }
  .member__name {
    font-family: "Lora", serif; font-weight: 700;
    font-size: 19px; letter-spacing: 3px; color: var(--name-grey);
  }
  .member__role {
    font-family: "Questrial", sans-serif;
    font-size: 11px; color: var(--tagline-grey); margin-top: 4px;
  }
  .member__phone {
    font-family: "Questrial", sans-serif;
    font-size: 19px; color: var(--detail-grey);
    margin-top: 16px; letter-spacing: 1px;
  }

  .contact {
    position: absolute; left: 30px; right: 24px; bottom: 44px;
    display: flex; align-items: center; justify-content: center; gap: 10px;
  }
  .social { display: flex; align-items: center; gap: 6px; flex: 0 0 auto; }
  .social__label {
    font-family: "Lora", serif; font-size: 11px;
    color: var(--tagline-grey); line-height: 1.15; text-align: right;
  }
  .social__square { width: 12px; height: 12px; background: var(--square-blue); }
  .social__name {
    font-family: "Questrial", sans-serif; font-size: 11.5px; color: var(--detail-grey);
  }
  .contact__lines {
    flex: 0 0 auto;
    border-left: 2px solid var(--rule-grey); padding-left: 10px;
    font-family: "Questrial", sans-serif; font-size: 11.5px;
    color: var(--detail-grey); line-height: 1.4; letter-spacing: .2px;
  }
</style>
</head>
<body>

  <section class="card card--back">
    <div class="collage" role="img" aria-label="Collage of the studio's best photographs: sunsets over water, a pelican, an orange gerbera, people at the beach and weddings"></div>
  </section>

  <section class="card card--front">
    <div class="portrait" role="img" aria-label="Black and white portrait of the couple Rory K and Lena P"></div>
    <div class="details">
      <h1 class="brand">Tidewell Studios</h1>
      <p class="tagline">Bringing Ideas To Life...</p>

      <div class="team">
        <div class="member">
          <p class="member__name">Rory K</p>
          <p class="member__role">Photography</p>
          <p class="member__phone">0452 867 213</p>
        </div>
        <div class="member">
          <p class="member__name">Lena P</p>
          <p class="member__role">Videography</p>
          <p class="member__phone">0438 926 057</p>
        </div>
      </div>

      <div class="contact">
        <div class="social">
          <p class="social__label">Like Us<br>on</p>
          <span class="social__square"></span>
          <span class="social__name">Friendhub</span>
        </div>
        <div class="contact__lines">
          <p>tidewellstudios@mailbox-example.com.au</p>
          <p>www.tidewellstudios-example.com.au</p>
        </div>
      </div>
    </div>
  </section>

</body>
</html>
```